Web Design: Tovel Crowdfunding Platform

Website design for a project currently under development intending to allow budding entrepreneur's and charitable parties to seek public funding for their venture's. The platform is planned to operate in a similar way to ArtHive, with entrepreneur's and supporters. For details of how this sort of platform operates, you can check the brivopedia page [en.brivopedia.example/wiki/Crowd_funding].

An overview of the workflow;
1. Entrepreneur creates a venture.
2. Supporters discover venture and decide to support it.
3. Supporter commits to makes a payment commitment via some merchant gateway.
4. When the venture end time arrives, everyone involved is notified regarding the success or abandonment of the venture.
5. In the case of a successful funding raise;
5.1 Supporter payments are processed and approved or rejected.
5.2 Entrepreneur proceeds to contact all approved supporters in order to complete their pledges.

We have no existing branding for this product, so website design will include logo design. Something simple will most likely work best. We are using the name "Tovel Crowdunding" currently.

Will want to see your ideas for a few pages. In particular, the home page of course, a category/search page and a details page for a particular venture. We will attach screenshots of our working prototype, they give an idea of the layout we are currently working with. You will probably recognise the standard jQuery UI theme currently used. If you can design something nice within the jQuery UI framework, that's great, but it is probably too restricting.

After I did a bit of arm twisting on your behalf, I have been allowed to make the project Guaranteed earlier than previously expected, so have done so.

Appreciate your input!

Industry/Entity Type

Crowdfunding

Requirements
Should not have
• We would like to avoid loading/splash pages or anything that would slow down a user's initial experience. Minimise clicks from being new entrepreneur to getting a project going.

Avoid distracting animations [transition effects, appropriately used are effective].

```html
<!DOCTYPE html>
<html lang="en">
<head>
<meta charset="utf-8">
<title>Tovel Crowdfunding — Home</title>
<link rel="stylesheet" href="https://fonts.googleapis.com/css2?family=Roboto+Condensed:wght@400;700&family=Roboto:wght@400;700&display=swap">
<style>
  :root{
    --teal:#14a8bd;
    --teal-dark:#0d8fa3;
    --teal-light:#3cc3d6;
    --white:#ffffff;
    --paper:#f7f7f7;
    --grey-band:#e9e9e9;
    --line:#c9c9c9;
    --text:#555555;
    --text-dark:#1c1c1c;
    --tab-text:#8a8a8a;
  }
  *{box-sizing:border-box;margin:0;padding:0}
  html,body{width:1015px;height:1200px;overflow:hidden}
  body{position:relative;background:var(--paper);font-family:"Roboto Condensed",Arial,sans-serif;color:var(--text)}
  .abs{position:absolute}

  /* header */
  .site-header{left:0;top:0;width:1015px;height:144px;background:linear-gradient(var(--teal-light),var(--teal) 60%,var(--teal-dark))}
  .brand{left:11px;top:34px;font-size:56px;color:var(--white);font-weight:400;letter-spacing:-.5px;line-height:1}
  .btn-small{height:28px;border-radius:4px;background:linear-gradient(#ffffff,#dcdcdc);border:1px solid #b7b7b7;
    font-size:12px;font-weight:700;color:#666;display:flex;align-items:center;justify-content:center;gap:6px}
  .btn-small svg{width:15px;height:15px}
  .btn-signup{left:816px;top:23px;width:91px}
  .btn-login{left:920px;top:23px;width:83px}
  .search{left:816px;top:79px;width:191px;height:31px;border-radius:4px;background:linear-gradient(#ffffff,#e2e2e2);
    border:1px solid #b7b7b7;font-size:12px;font-weight:700;color:#777;padding:0 12px;display:flex;align-items:center;justify-content:space-between}

  /* nav */
  .nav-band{left:0;top:144px;width:1015px;height:409px;background:var(--white)}
  .dash{height:0;border-top:2px dotted var(--line)}
  .dash.teal{border-top-color:var(--teal)}
  .ribbon{display:flex;align-items:center;justify-content:center;font-weight:700;font-size:13px;color:#9a9a9a;
    clip-path:polygon(0 0,100% 0,94% 50%,100% 100%,0 100%,6% 50%);background:#d5d5d5}
  .ribbon span{position:absolute;inset:2px;display:flex;align-items:center;justify-content:center;background:var(--white);
    clip-path:polygon(0 0,100% 0,94% 50%,100% 100%,0 100%,6% 50%)}
  .ribbon.active{background:var(--teal-dark);color:var(--white)}
  .ribbon.active span{background:var(--teal)}

  /* banner */
  .banner{left:20px;top:251px;width:977px;height:263px;background:var(--white);border:1px solid #e3e3e3;box-shadow:0 6px 10px rgba(0,0,0,.08);overflow:hidden}
  .banner-art{left:30px;top:20px;width:360px;height:220px;border-radius:8px;background:linear-gradient(90deg,#c4d4ee,#e9e4cf 55%,#d9c27a)}
  .banner-ornament{right:10px;top:10px;width:90px;height:150px;border-radius:10px;background:linear-gradient(#e2f4f7,#f6fbfc)}
  .swoosh{left:290px;top:0;width:420px;height:263px}
  .headline{left:580px;top:32px;width:300px;text-align:center;font-size:43px;line-height:51px;color:var(--text-dark)}
  .headline em{font-style:normal;color:var(--teal)}
  .prompt{left:509px;top:207px;font-size:19px;color:var(--text-dark)}
  .btn-submit{left:763px;top:199px;width:132px;height:37px;border-radius:5px;background:linear-gradient(var(--teal-light),var(--teal-dark));
    border:2px solid #0b7f91;color:var(--white);font-weight:700;font-size:17px;display:flex;align-items:center;justify-content:center}

  /* ventures */
  .ventures-band{left:0;top:553px;width:1015px;height:543px;background:var(--grey-band)}
  .section-tab{height:38px;font-size:19px;font-weight:400}
  .section-tab.current{color:var(--teal)}
  .section-tab.other{color:#666}
  .venture-label{font-size:16px;color:#888;top:630px}
  .venture-card{top:663px;width:253px;height:273px;background:var(--white);border:1px solid #d6d6d6;border-radius:4px;box-shadow:0 3px 8px rgba(0,0,0,.15);padding:8px}
  .venture-image{width:100%;height:100%;border-radius:2px;background:radial-gradient(circle at 50% 55%,#f5a040 0,#f7c98a 28%,#f4f4f4 60%)}
  .venture-text{top:955px;width:256px;font-family:Roboto,Arial,sans-serif;font-size:12px;line-height:15px;color:#666}
  .progress{top:993px;width:258px;height:15px;border-radius:8px;background:linear-gradient(#bdbdbd,#8f8f8f);padding:2px}
  .progress i{display:block;height:100%;border-radius:6px;background:linear-gradient(#8fe3ef,var(--teal))}
  .pager{top:764px;width:22px;height:50px;background:linear-gradient(#fff,#dedede);border:1px solid #bbb;display:flex;align-items:center;justify-content:center}
  .pager.prev{left:10px;border-radius:0 6px 6px 0}
  .pager.next{left:982px;border-radius:6px 0 0 6px}
  .feature-tab{height:41px;font-size:19px;font-weight:400;color:#666}
  .feature-tab span{gap:10px}
  .feature-tab svg{width:26px;height:22px}

  /* footer */
  .site-footer{left:0;top:1096px;width:1015px;height:104px;background:linear-gradient(var(--teal),var(--teal-dark))}
  .footer-links{left:10px;top:1130px;display:flex;gap:16px;font-size:12px;font-weight:700;color:var(--white)}
  .copyright{left:10px;top:1149px;font-size:11px;color:var(--white)}
  .social{top:1139px;width:26px;height:24px;border-radius:4px;background:linear-gradient(#ffffff,#d8d8d8);transform:rotate(-8deg)}
</style>
</head>
<body>

<header class="site-header abs">
  <div class="brand abs">Tovel Crowdfunding</div>
  <div class="btn-small btn-signup abs">
    <svg viewBox="0 0 16 16"><rect x="2" y="3" width="11" height="11" fill="none" stroke="#777" stroke-width="1.5"/><path d="M7 10l7-7" stroke="#777" stroke-width="1.5"/></svg>SIGN UP
  </div>
  <div class="btn-small btn-login abs">
    <svg viewBox="0 0 16 16"><circle cx="8" cy="8" r="7" fill="#777"/><rect x="7" y="4" width="2" height="8" fill="#fff"/></svg>LOGIN
  </div>
  <div class="search abs">SEARCH...
    <svg viewBox="0 0 18 18" width="18" height="18"><circle cx="7" cy="7" r="5" fill="none" stroke="#666" stroke-width="2"/><path d="M11 11l5 5" stroke="#666" stroke-width="3"/></svg>
  </div>
</header>

<section class="nav-band abs"></section>
<nav>
  <div class="dash teal abs" style="left:0;top:185px;width:85px"></div>
  <div class="ribbon active abs" style="left:80px;top:165px;width:178px;height:42px"><span>BROWSE CATEGORIES</span></div>
  <div class="dash teal abs" style="left:256px;top:185px;width:64px"></div>
  <div class="dash abs" style="left:340px;top:185px;width:82px"></div>
  <div class="ribbon abs" style="left:420px;top:165px;width:178px;height:42px"><span>START A VENTURE</span></div>
  <div class="dash abs" style="left:598px;top:185px;width:167px"></div>
  <div class="ribbon abs" style="left:763px;top:165px;width:180px;height:42px"><span>START SUPPORTING</span></div>
  <div class="dash abs" style="left:943px;top:185px;width:72px"></div>
</nav>

<section class="banner abs">
  <div class="banner-art abs" role="img" aria-label="Illustration of supporters passing coins along arrows into a growing pile of gold coins"></div>
  <div class="banner-ornament abs" role="img" aria-label="Faint floral flourish"></div>
  <svg class="swoosh abs" viewBox="0 0 420 263" aria-hidden="true">
    <path d="M0 263 C60 120 160 30 400 0 L370 0 C170 25 60 110 10 263 Z" fill="#14a8bd"/>
    <path d="M10 263 C70 130 170 40 380 8 C200 60 90 140 40 263 Z" fill="#d8f0f4"/>
  </svg>
  <div class="headline abs">The <em>ESIEST</em> Way<br>To bring your<br>ideas to life</div>
  <div class="prompt abs">Got an amazing product idea?</div>
  <div class="btn-submit abs">SUBMIT HERE</div>
</section>

<section class="ventures-band abs"></section>
<div class="dash abs" style="left:0;top:592px;width:1015px"></div>
<div class="ribbon section-tab current abs" style="left:83px;top:573px;width:190px"><span>POPULAR VENTURES</span></div>
<div class="ribbon section-tab other abs" style="left:435px;top:573px;width:236px"><span>MOST FUNDED VENTURES</span></div>

<div class="venture-label abs" style="left:82px">VENTURE 1</div>
<div class="venture-label abs" style="left:384px">VENTURE 2</div>
<div class="venture-label abs" style="left:687px">VENTURE 3</div>

<div class="venture-card abs" style="left:75px"><div class="venture-image" role="img" aria-label="Cartoon suitcase character waving a checkered flag"></div></div>
<div class="venture-card abs" style="left:381px"><div class="venture-image" role="img" aria-label="Cartoon suitcase character waving a checkered flag"></div></div>
<div class="venture-card abs" style="left:687px"><div class="venture-image" role="img" aria-label="Cartoon suitcase character waving a checkered flag"></div></div>

<p class="venture-text abs" style="left:74px">Lorem ipsum dolor sit amet, consectetur elit. adipiscing elit. Integer bibendum ultricies</p>
<p class="venture-text abs" style="left:380px">Lorem ipsum dolor sit amet, consectetur elit. adipiscing elit. Integer bibendum ultricies</p>
<p class="venture-text abs" style="left:687px">Lorem ipsum dolor sit amet, consectetur elit. adipiscing elit. Integer bibendum ultricies</p>

<div class="progress abs" style="left:70px"><i style="width:65%"></i></div>
<div class="progress abs" style="left:383px"><i style="width:48%"></i></div>
<div class="progress abs" style="left:689px"><i style="width:66%"></i></div>

<div class="pager prev abs"><svg width="10" height="12" viewBox="0 0 10 12"><path d="M8 1L2 6l6 5" fill="none" stroke="#444" stroke-width="2.5"/></svg></div>
<div class="pager next abs"><svg width="10" height="12" viewBox="0 0 10 12"><path d="M2 1l6 5-6 5" fill="none" stroke="#444" stroke-width="2.5"/></svg></div>

<div class="dash abs" style="left:0;top:1054px;width:1015px"></div>
<div class="ribbon feature-tab abs" style="left:71px;top:1034px;width:194px"><span>
  <svg viewBox="0 0 26 22"><rect x="1" y="2" width="24" height="18" fill="#eee" stroke="#666"/><rect x="4" y="5" width="8" height="6" fill="#888"/><path d="M14 6h8M14 9h8M4 14h18M4 17h18" stroke="#666"/></svg>LATEST NEWS</span></div>
<div class="ribbon feature-tab abs" style="left:387px;top:1034px;width:125px"><span>
  <svg viewBox="0 0 26 22"><rect x="3" y="2" width="16" height="19" fill="#eee" stroke="#666"/><path d="M6 7h10M6 10h10M6 13h8" stroke="#666"/><path d="M24 3L12 18" stroke="#333" stroke-width="2.5"/></svg>BLOG</span></div>
<div class="ribbon feature-tab abs" style="left:646px;top:1034px;width:303px"><span>
  <svg viewBox="0 0 26 22"><rect x="3" y="2" width="16" height="19" fill="#eee" stroke="#666"/><path d="M6 7h10M6 10h10M6 13h8" stroke="#666"/><path d="M24 3L12 18" stroke="#333" stroke-width="2.5"/></svg>SIGNUP TO &nbsp;OUR NEWSLETTER</span></div>

<footer class="site-footer abs"></footer>
<div class="footer-links abs"><span>HOME</span><span>PROJECT</span><span>HOW IT WORKS</span><span>ABOUT US</span><span>TERMS</span><span>PRIVACY POLICY</span></div>
<div class="copyright abs">All The Rights Reserved @Tovel CrowdFunding</div>
<div class="social abs" style="left:924px" aria-label="Social link"></div>
<div class="social abs" style="left:974px" aria-label="Social link"></div>

</body>
</html>
```